Flyer for Lawnmowing and gardening business

We are a lawn mowing and gardening business needing a flyer designed listing our services and business info.
The flyer should include all business information and contact details as below.

Lawn mowing
Gardening
Green waste removal
Pruning
Weeding
Vegetable Garden Creation

Phone number:0481657240

As well as the logo provided

Target Market(s)

Local people wanting someone to care for their garden.

Industry/Entity Type

Gardener

Font styles to use
Serif

Requirements
Must have
• Business Logo
• All business info and services provided. EG
• Lawn mowing
• Gardening
• Green waste removal
• Pruning
• Weeding
• Vegetable Garden Creation
• Phone number:0481657240
Nice to have
• Earthy tones, clean and simple flyer design

```html
<!DOCTYPE html>
<html lang="en">
<head>
<meta charset="utf-8">
<title>Fernbrook Lawns – Lawn Mowing &amp; Garden Care</title>
<link href="https://fonts.googleapis.com/css2?family=Libre+Baskerville:wght@400;700&display=swap" rel="stylesheet">
<style>
  :root {
    --paper: #ffffff;
    --brown-dark: #4e3119;
    --brown-mid: #8a5a34;
    --rust: #a8652c;
    --beige: #ddd3ac;
    --text-dark: #3a2412;
    --leaf: #5f8a2e;
    --white: #ffffff;
  }
  * { margin: 0; padding: 0; box-sizing: border-box; }
  html, body { width: 1200px; height: 2486px; overflow: hidden; background: var(--paper); }
  .flyer {
    position: relative;
    width: 1200px;
    height: 2486px;
    overflow: hidden;
    background: var(--paper);
    font-family: "Libre Baskerville", Georgia, serif;
  }
  .brand {
    position: absolute;
    top: 170px;
    left: 0;
    width: 1200px;
    text-align: center;
    color: var(--brown-dark);
  }
  .brand-mark {
    display: inline-block;
    width: 70px;
    height: 70px;
    border-radius: 50%;
    background: var(--leaf);
    margin-bottom: 22px;
  }
  .brand-name {
    font-size: 62px;
    font-weight: 400;
    letter-spacing: 2px;
    line-height: 1;
  }
  .brand-tagline {
    margin-top: 14px;
    font-size: 34px;
    color: var(--leaf);
    letter-spacing: 1px;
  }
  .hero-photo {
    position: absolute;
    top: 470px;
    left: 0;
    width: 1200px;
    height: 1000px;
    background:
      linear-gradient(180deg, #c9dbe8 0%, #8fae6a 30%, #4f7a2a 62%, #3b6020 100%);
  }
  .swooshes {
    position: absolute;
    top: 0;
    left: 0;
    width: 1200px;
    height: 2486px;
  }
  .services {
    position: absolute;
    top: 1595px;
    left: 150px;
    list-style: none;
  }
  .service {
    display: flex;
    align-items: center;
    height: 90px;
    font-size: 54px;
    font-weight: 700;
    color: var(--text-dark);
  }
  .service-tick {
    width: 44px;
    height: 44px;
    margin-right: 46px;
    flex: none;
  }
  .phone-band {
    position: absolute;
    left: 0;
    bottom: 0;
    width: 1200px;
    height: 275px;
    background: var(--brown-mid);
    display: flex;
    align-items: center;
    justify-content: center;
  }
  .phone-number {
    color: var(--white);
    font-size: 92px;
    font-weight: 700;
    letter-spacing: 2px;
  }
</style>
</head>
<body>
<main class="flyer">
  <header class="brand">
    <span class="brand-mark"></span>
    <div class="brand-name">Fernbrook Lawns</div>
    <div class="brand-tagline">Lawn Mowing &amp; Garden Care</div>
  </header>

  <div class="hero-photo" role="img" aria-label="Photo of a blue lawn mower cutting green grass in a sunny garden with trees behind"></div>

  <svg class="swooshes" viewBox="0 0 1200 2486" aria-hidden="true">
    <!-- top edge of photo -->
    <path d="M0 470 L1200 470 L1200 520 C900 470 500 470 0 560 Z" fill="var(--paper)"/>
    <path d="M0 490 C420 430 800 455 1200 455 L1200 478 C820 480 420 470 0 540 Z" fill="var(--brown-dark)"/>
    <path d="M0 545 C400 470 820 485 1200 490 L1200 500 C820 500 420 490 0 560 Z" fill="var(--rust)"/>
    <!-- bottom edge of photo -->
    <path d="M0 1380 C300 1330 700 1310 1200 1330 L1200 1352 C700 1340 320 1360 0 1410 Z" fill="var(--rust)"/>
    <path d="M0 1420 C350 1360 760 1360 1200 1390 L1200 1480 L0 1480 Z" fill="var(--brown-dark)"/>
    <path d="M0 1470 C380 1420 780 1420 1200 1450 L1200 2212 L0 2212 Z" fill="var(--beige)"/>
  </svg>

  <ul class="services">
    <li class="service"><svg class="service-tick" viewBox="0 0 24 24"><path d="M3 13 L9 19 L21 5" fill="none" stroke="var(--brown-dark)" stroke-width="3" stroke-linecap="round" stroke-linejoin="round"/></svg>Lawn mowing</li>
    <li class="service"><svg class="service-tick" viewBox="0 0 24 24"><path d="M3 13 L9 19 L21 5" fill="none" stroke="var(--brown-dark)" stroke-width="3" stroke-linecap="round" stroke-linejoin="round"/></svg>Gardening</li>
    <li class="service"><svg class="service-tick" viewBox="0 0 24 24"><path d="M3 13 L9 19 L21 5" fill="none" stroke="var(--brown-dark)" stroke-width="3" stroke-linecap="round" stroke-linejoin="round"/></svg>Green waste removal</li>
    <li class="service"><svg class="service-tick" viewBox="0 0 24 24"><path d="M3 13 L9 19 L21 5" fill="none" stroke="var(--brown-dark)" stroke-width="3" stroke-linecap="round" stroke-linejoin="round"/></svg>Pruning</li>
    <li class="service"><svg class="service-tick" viewBox="0 0 24 24"><path d="M3 13 L9 19 L21 5" fill="none" stroke="var(--brown-dark)" stroke-width="3" stroke-linecap="round" stroke-linejoin="round"/></svg>Weeding</li>
    <li class="service"><svg class="service-tick" viewBox="0 0 24 24"><path d="M3 13 L9 19 L21 5" fill="none" stroke="var(--brown-dark)" stroke-width="3" stroke-linecap="round" stroke-linejoin="round"/></svg>Vegetable Garden Creation</li>
  </ul>

  <footer class="phone-band">
    <div class="phone-number">PH: 0481657240</div>
  </footer>
</main>
</body>
</html>
```